Coralwind Gulfside LLC

we need a business card design

Industry/Entity Type

hvac

Contact Information for Business Card

my logo

Requirements
Must have
• my logo and same colors

```html
<!DOCTYPE html>
<html lang="en">
<head>
<meta charset="UTF-8">
<title>Coralwind Gulfside LLC — Business Card</title>
<link href="https://fonts.googleapis.com/css2?family=Oswald:wght@600&family=Poppins:wght@500;700&display=swap" rel="stylesheet">
<style>
  :root {
    --backdrop: #d3d4d6;
    --card-white: #ffffff;
    --brand-blue: #0a58a0;
    --brand-blue-deep: #084f93;
    --brand-orange: #f6a93b;
    --text-white: #ffffff;
  }
  * { margin: 0; padding: 0; box-sizing: border-box; }
  html, body { width: 900px; height: 1200px; overflow: hidden; }
  body { background: var(--backdrop); position: relative; font-family: "Poppins", sans-serif; }

  .card { position: absolute; left: 135px; width: 630px; height: 357px; overflow: hidden; }
  .card-front { top: 214px; background: var(--card-white); }
  .card-back {
    top: 628px;
    background: linear-gradient(160deg, var(--brand-blue) 0%, var(--brand-blue-deep) 100%);
  }

  .brand-name {
    position: absolute;
    font-family: "Poppins", sans-serif;
    font-weight: 700;
    text-align: center;
    line-height: 1.1;
    text-transform: uppercase;
    letter-spacing: 1px;
  }
  .card-front .brand-name {
    left: 0; width: 630px; top: 132px;
    font-size: 34px; color: var(--brand-blue);
  }
  .card-back .brand-name {
    left: 330px; width: 260px; top: 80px;
    font-size: 24px; color: var(--text-white);
  }

  .service-line {
    position: absolute; left: 0; width: 630px; top: 313px;
    text-align: center;
    font-family: "Oswald", sans-serif; font-weight: 600;
    font-size: 13px; color: var(--brand-blue);
    letter-spacing: -0.1px;
  }

  .holder { position: absolute; left: 39px; top: 168px; }
  .holder-name {
    font-weight: 700; font-size: 25px; color: var(--brand-orange);
    line-height: 1.1;
  }
  .holder-role { font-weight: 500; font-size: 15px; color: var(--text-white); margin-top: 2px; }
  .holder-rule { width: 49px; height: 3px; background: var(--brand-orange); margin-top: 8px; }

  .contact-list { position: absolute; left: 39px; top: 243px; list-style: none; }
  .contact-list li {
    display: flex; align-items: center; gap: 8px;
    font-weight: 500; font-size: 15.5px; color: var(--text-white);
    height: 28px;
  }
  .contact-list .phone-number { letter-spacing: 2.5px; }
  .contact-icon { width: 15px; height: 15px; flex: none; }
</style>
</head>
<body>

  <section class="card card-front">
    <div class="brand-name">Coralwind<br>Gulfside LLC</div>
    <p class="service-line">FREE AC SERVICE CALLS WITH REPAIRS - SAME DAY AC REPAIRS, NEXT DAY AIR CONDITIONING INSTALLATION</p>
  </section>

  <section class="card card-back">
    <div class="brand-name">Coralwind<br>Gulfside LLC</div>

    <div class="holder">
      <div class="holder-name">DANIEL MORROW</div>
      <div class="holder-role">Owner</div>
      <div class="holder-rule"></div>
    </div>

    <ul class="contact-list">
      <li>
        <svg class="contact-icon" viewBox="0 0 24 24" aria-hidden="true">
          <path fill="#f6a93b" d="M6.6 10.8a15.1 15.1 0 0 0 6.6 6.6l2.2-2.2c.3-.3.7-.4 1-.2 1.1.4 2.3.6 3.6.6.6 0 1 .4 1 1V20c0 .6-.4 1-1 1A17 17 0 0 1 3 4c0-.6.4-1 1-1h3.5c.6 0 1 .4 1 1 0 1.3.2 2.5.6 3.6.1.3 0 .7-.2 1z"/>
        </svg>
        <span class="phone-number">727-555-0148</span>
      </li>
      <li>
        <svg class="contact-icon" viewBox="0 0 24 24" aria-hidden="true">
          <rect x="2" y="5" width="20" height="14" fill="#f6a93b"/>
          <path d="M2 5l10 8 10-8" fill="none" stroke="#0a58a0" stroke-width="1.8"/>
        </svg>
        <span>dan@coralwindgulfside.com</span>
      </li>
      <li>
        <svg class="contact-icon" viewBox="0 0 24 24" aria-hidden="true">
          <g fill="none" stroke="#f6a93b" stroke-width="1.8">
            <circle cx="12" cy="12" r="9.5"/>
            <ellipse cx="12" cy="12" rx="4.2" ry="9.5"/>
            <path d="M2.5 12h19M4 7h16M4 17h16"/>
          </g>
        </svg>
        <span>coralwindgulfside.com</span>
      </li>
    </ul>
  </section>

</body>
</html>
```